Proposal Poster, posters for kids to hold

I am proposing to my girlfriend soon, I need two posters made for my kids to hold one I want to say “be my mommy”
And the other “will you marry my daddy”
Both in horizontal format. I plan on sending the files to a print shop to get them printed on a large poster. Simple is fine with maybe a few graphics. Open to anything. Kids will be holding it from the beach as we are on a jet ski close to shore. Must be readable font from a short distance

• Cute but readable font from a distance

```html
<!DOCTYPE html>
<html lang="en">
<head>
<meta charset="utf-8">
<title>Proposal Posters</title>
<link rel="stylesheet" href="https://fonts.googleapis.com/css2?family=Yellowtail&display=swap">
<style>
  :root {
    --backdrop: #808080;
    --poster-pink: #ec8f98;
    --letter-white: #ffffff;
    --ink-black: #000000;
    --ring-tone: #c9dde8;
    --heart-tone: #c21f78;
  }
  html, body {
    margin: 0;
    padding: 0;
    width: 1200px;
    height: 960px;
    overflow: hidden;
    background: var(--backdrop);
  }
  .canvas {
    position: relative;
    width: 1200px;
    height: 960px;
  }
  .poster {
    position: absolute;
    left: 316px;
    width: 574px;
    height: 430px;
    background: var(--poster-pink);
    overflow: hidden;
  }
  .poster--daddy { top: 58px; }
  .poster--mommy { top: 506px; }
  .poster-art {
    display: block;
    width: 574px;
    height: 430px;
  }
  .script-line {
    font-family: "Yellowtail", "Brush Script MT", cursive;
    font-weight: 400;
    fill: var(--letter-white);
    stroke: var(--ink-black);
    stroke-width: 5px;
    stroke-linejoin: round;
    paint-order: stroke fill;
    filter: drop-shadow(5px 5px 0 var(--ink-black));
  }
  .line-will-you { font-size: 130px; }
  .line-marry-my { font-size: 118px; }
  .line-daddy    { font-size: 150px; }
  .line-be-my    { font-size: 180px; }
  .line-mommy    { font-size: 160px; }
  .ring-art  { fill: var(--ring-tone); }
  .heart-art { fill: var(--heart-tone); }
</style>
</head>
<body>
<main class="canvas">
  <section class="poster poster--daddy">
    <svg class="poster-art" viewBox="0 0 574 430">
      <rect class="ring-art" x="14" y="294" width="96" height="116" rx="18" role="img" aria-label="Illustration of a diamond engagement ring"/>
      <text class="script-line line-will-you" x="30" y="138" textLength="470" lengthAdjust="spacingAndGlyphs">Will You</text>
      <text class="script-line line-marry-my" x="42" y="226" textLength="445" lengthAdjust="spacingAndGlyphs">marry my</text>
      <text class="script-line line-daddy" x="122" y="362" textLength="425" lengthAdjust="spacingAndGlyphs">Daddy?</text>
    </svg>
  </section>

  <section class="poster poster--mommy">
    <svg class="poster-art" viewBox="0 0 574 430">
      <rect class="heart-art" x="240" y="206" width="104" height="46" rx="14" role="img" aria-label="Illustration of a glossy magenta heart"/>
      <text class="script-line line-be-my" x="30" y="196" textLength="485" lengthAdjust="spacingAndGlyphs">Be my</text>
      <text class="script-line line-mommy" x="36" y="372" textLength="500" lengthAdjust="spacingAndGlyphs">Mommy</text>
    </svg>
  </section>
</main>
</body>
</html>
```